Hearing Assessments & Hearing Aids

I need a business card design for my new business called 'Meridian Hearing Aids & Audiometry. I do hearing assessments for adults and children. I also fit hearing aids to hearing impaired people. I would also like to incorporate in my business card Aboriginal designs and colours with a picture of an ear which represents my hearing business as well as my Aboriginal culture.

I would also like my profession added to the business card. I am an Audioetrist.

Target Market(s)

My target customers are everyone concerned with theri hearing and for those who require hearing aids

Industry/Entity Type

Business

Contact Information for Business Card

Meridian Hearing Aids & Audiometry
Dana Forsythe
0412 309 645

Requirements
Must have
• Meridian Hearing Aids & Audiometry
Dana FOrsythe
Mobile: 0412 309 645
Email: danaforsythe07@quillmail.com

Audiometrist

```html
<!DOCTYPE html>
<html lang="en">
<head>
<meta charset="utf-8">
<title>Meridian Hearing Aids &amp; Audiometry – Business Card</title>
<link rel="stylesheet" href="https://fonts.googleapis.com/css2?family=Delius&display=swap">
<style>
  :root {
    --stage: #c8c8c8;
    --card: #c4a55f;
    --cream: #f6edc9;
    --ochre-red: #9b1f1a;
    --earth: #6b5633;
    --earth-dark: #5e4a2c;
    --band: #9a7440;
    --faint: #b8984f;
    --ink: #111111;
  }
  html, body {
    margin: 0;
    padding: 0;
    width: 1200px;
    height: 899px;
    overflow: hidden;
    background: var(--stage);
    font-family: "Delius", "Trebuchet MS", sans-serif;
  }
  .stage {
    position: relative;
    width: 1200px;
    height: 899px;
  }
  .card {
    position: absolute;
    top: 106px;
    width: 388px;
    height: 672px;
    background: var(--card);
    overflow: hidden;
  }
  .card--front { left: 153px; }
  .card--back { left: 691px; }

  .ear-motif {
    position: absolute;
    left: 87px;
    top: 59px;
    width: 216px;
    height: 366px;
  }
  .front-title {
    position: absolute;
    left: 0;
    width: 100%;
    top: 484px;
    margin: 0;
    text-align: center;
    color: var(--cream);
    font-weight: 400;
    font-size: 33px;
    line-height: 46px;
  }
  .dot-band {
    position: absolute;
    height: 12px;
  }
  .card--front .dot-band { left: 83px; top: 606px; width: 222px; }

  .ear-motif--faint {
    position: absolute;
    left: 188px;
    top: 0;
    width: 200px;
    height: 345px;
  }
  .back-title {
    position: absolute;
    left: 32px;
    top: 92px;
    margin: 0;
    color: var(--cream);
    font-weight: 400;
    font-size: 29px;
    line-height: 40px;
  }
  .card--back .dot-band--upper { left: 23px; top: 390px; width: 170px; }
  .card--back .dot-band--lower { left: 195px; top: 600px; width: 172px; }
  .holder-name {
    position: absolute;
    left: 23px;
    top: 426px;
    margin: 0;
    color: var(--ochre-red);
    font-weight: 400;
    font-size: 39px;
    line-height: 50px;
  }
  .holder-role {
    position: absolute;
    left: 23px;
    top: 478px;
    margin: 0;
    color: var(--cream);
    font-size: 18px;
    letter-spacing: 0.5px;
  }
  .holder-contact {
    position: absolute;
    left: 23px;
    top: 510px;
    margin: 0;
    color: var(--earth-dark);
    font-size: 18px;
    line-height: 28px;
    letter-spacing: 0.5px;
  }
  .holder-contact span { display: block; }
  .side-label {
    position: absolute;
    top: 824px;
    width: 388px;
    margin: 0;
    text-align: center;
    color: var(--ink);
    font-size: 21px;
  }
  .side-label--front { left: 153px; }
  .side-label--back { left: 691px; }
</style>
</head>
<body>
<main class="stage">
  <section class="card card--front">
    <svg class="ear-motif" role="img" aria-label="Aboriginal dot-painting style ear motif in earth brown with an ochre red curve and lobe" viewBox="0 0 216 366">
      <defs>
        <linearGradient id="earTone" x1="0" y1="0" x2="0.4" y2="1">
          <stop offset="0%" stop-color="#6b5633"/>
          <stop offset="55%" stop-color="#7d4a2c"/>
          <stop offset="100%" stop-color="#9b1f1a"/>
        </linearGradient>
      </defs>
      <path d="M108 4 C176 4 214 52 214 110 C214 170 176 200 150 240 C130 272 120 320 100 350 C86 366 60 366 52 348 C42 324 30 290 30 250 C30 200 2 170 2 112 C2 50 48 4 108 4 Z" fill="url(#earTone)" opacity="0.85"/>
    </svg>
    <h1 class="front-title">Meridian Hearing Aids<br>&amp; Audiometry</h1>
    <svg class="dot-band" role="img" aria-label="Dotted wave border pattern" viewBox="0 0 222 12" preserveAspectRatio="none">
      <rect width="222" height="12" rx="6" fill="var(--band)"/>
    </svg>
  </section>

  <section class="card card--back">
    <svg class="ear-motif--faint" role="img" aria-label="Faint dot-painting style ear motif" viewBox="0 0 200 345">
      <path d="M100 0 C162 0 200 44 200 100 C200 156 166 184 142 222 C122 254 112 300 94 330 C80 348 56 348 48 330 C38 306 28 276 28 238 C28 190 0 160 0 104 C0 46 42 0 100 0 Z" fill="var(--faint)" opacity="0.7"/>
    </svg>
    <h2 class="back-title">Meridian Hearing Aids<br>&amp; Audiometry</h2>
    <svg class="dot-band dot-band--upper" role="img" aria-label="Dotted wave border pattern" viewBox="0 0 170 12" preserveAspectRatio="none">
      <rect width="170" height="12" rx="6" fill="var(--band)"/>
    </svg>
    <p class="holder-name">Dana Forsythe</p>
    <p class="holder-role">Audiometrist</p>
    <p class="holder-contact">
      <span>Mobile: 0412 309 645</span>
      <span>danaforsythe07@quillmail.com</span>
    </p>
    <svg class="dot-band dot-band--lower" role="img" aria-label="Dotted wave border pattern" viewBox="0 0 172 12" preserveAspectRatio="none">
      <rect width="172" height="12" rx="6" fill="var(--band)"/>
    </svg>
  </section>

  <p class="side-label side-label--front">Front side</p>
  <p class="side-label side-label--back">Back side</p>
</main>
</body>
</html>
```